Sign Design

We already have a logo, but would like to design 2 x signs.
Sign 1:
Dimensions 1500mm wide x 2500m high.
Information to include on sign: - Clinic name and logo (attached)
- the word "DENTIST "
- Street number (which is 348)
Phone number (which is 6153 4097)

Sign 2:
Dimensions: 800mm wide x 600mm high

```html
<!DOCTYPE html>
<html lang="en">
<head>
<meta charset="utf-8">
<title>Willowbank Dental Care – Signage</title>
<link rel="stylesheet" href="https://fonts.googleapis.com/css2?family=Arimo:wght@400;700&display=swap">
<style>
  :root {
    --stage-dark: #2a2828;
    --stage-light: #4a4848;
    --sign-white: #ffffff;
    --brand-green: #1a6e3a;
    --mark-green: #1fae2a;
    --ink: #111111;
    --wash-blue: #3cc3e0;
    --wash-teal: #1f7f95;
    --wash-green: #9fd24f;
    --wash-yellow: #f3eaa0;
  }
  * { box-sizing: border-box; margin: 0; padding: 0; }
  html, body { width: 1200px; height: 960px; overflow: hidden; }
  body {
    position: relative;
    background: radial-gradient(ellipse at 50% 50%, var(--stage-light) 0%, var(--stage-dark) 70%);
    font-family: "Arimo", Arial, sans-serif;
  }
  .sign {
    position: absolute;
    background: var(--sign-white);
    overflow: hidden;
  }
  .sign__wash { position: absolute; inset: 0; width: 100%; height: 100%; }
  .sign--fascia { left: 34px; top: 166px; width: 1133px; height: 189px; }
  .sign--panel  { left: 298px; top: 392px; width: 605px; height: 453px; }

  .brand-mark {
    position: absolute;
    border-radius: 50%;
    background: var(--mark-green);
  }
  .brand-name {
    position: absolute;
    color: var(--brand-green);
    font-weight: 400;
    line-height: 1;
    white-space: nowrap;
  }
  .brand-name span { display: block; }

  /* Fascia sign */
  .sign--fascia .brand-mark { left: 52px; top: 40px; width: 104px; height: 104px; }
  .sign--fascia .brand-name { left: 190px; top: 40px; }
  .sign--fascia .brand-name__main { font-size: 60px; letter-spacing: -2.5px; }
  .sign--fascia .brand-name__sub  { font-size: 34px; letter-spacing: -1px; margin: 2px 0 0 104px; }

  .service-word {
    position: absolute;
    left: 560px; top: 70px;
    font-size: 50px;
    font-weight: 400;
    color: var(--ink);
    letter-spacing: 1px;
    transform: rotate(-30deg);
    transform-origin: center;
  }
  .contact {
    position: absolute;
    left: 900px; top: 28px;
    width: 200px;
    text-align: center;
    color: var(--ink);
  }
  .contact__label { font-size: 21px; line-height: 1; }
  .contact__value { font-size: 28px; font-weight: 700; line-height: 1; margin: 6px 0 26px; }

  /* Panel sign */
  .sign--panel .brand-mark { left: 212px; top: 88px; width: 180px; height: 180px; }
  .sign--panel .brand-name { left: 180px; top: 276px; text-align: right; }
  .sign--panel .brand-name__main { font-size: 72px; letter-spacing: -3px; margin-left: -48px; }
  .sign--panel .brand-name__sub  { font-size: 40px; letter-spacing: -1.2px; margin-top: 2px; margin-right: 26px; }
</style>
</head>
<body>

  <section class="sign sign--fascia" aria-label="Fascia sign">
    <svg class="sign__wash" viewBox="0 0 1133 189" preserveAspectRatio="none" aria-hidden="true">
      <defs>
        <filter id="soft-fascia" x="-20%" y="-50%" width="140%" height="200%">
          <feGaussianBlur stdDeviation="14"/>
        </filter>
      </defs>
      <g filter="url(#soft-fascia)" opacity="0.9">
        <ellipse cx="200" cy="150" rx="240" ry="14" fill="var(--wash-yellow)"/>
        <ellipse cx="130" cy="185" rx="260" ry="20" fill="var(--wash-blue)" opacity="0.6"/>
        <ellipse cx="600" cy="165" rx="330" ry="26" fill="var(--wash-blue)"/>
        <ellipse cx="900" cy="110" rx="120" ry="14" fill="var(--wash-teal)"/>
        <ellipse cx="830" cy="150" rx="220" ry="24" fill="var(--wash-green)"/>
        <ellipse cx="1040" cy="185" rx="200" ry="18" fill="var(--wash-green)"/>
      </g>
      <rect x="856" y="0" width="277" height="189" fill="#ffffff" opacity="0.55"/>
    </svg>

    <div class="brand-mark" aria-hidden="true"></div>
    <h1 class="brand-name">
      <span class="brand-name__main">Willowbank</span>
      <span class="brand-name__sub">Dental Care</span>
    </h1>

    <p class="service-word">DENTIST</p>

    <div class="contact">
      <p class="contact__label">Street number</p>
      <p class="contact__value">348</p>
      <p class="contact__label">Phone number</p>
      <p class="contact__value">6153 4097</p>
    </div>
  </section>

  <section class="sign sign--panel" aria-label="Panel sign">
    <svg class="sign__wash" viewBox="0 0 605 453" preserveAspectRatio="none" aria-hidden="true">
      <defs>
        <filter id="soft-panel" x="-20%" y="-50%" width="140%" height="200%">
          <feGaussianBlur stdDeviation="16"/>
        </filter>
      </defs>
      <g filter="url(#soft-panel)" opacity="0.9">
        <ellipse cx="120" cy="60" rx="170" ry="14" fill="var(--wash-yellow)"/>
        <ellipse cx="250" cy="30" rx="260" ry="18" fill="var(--wash-blue)"/>
        <ellipse cx="480" cy="20" rx="200" ry="22" fill="var(--wash-green)"/>
        <ellipse cx="470" cy="90" rx="70" ry="18" fill="var(--wash-teal)"/>
        <ellipse cx="70" cy="365" rx="60" ry="18" fill="var(--wash-teal)"/>
        <ellipse cx="460" cy="385" rx="160" ry="12" fill="var(--wash-yellow)"/>
        <ellipse cx="260" cy="410" rx="280" ry="22" fill="var(--wash-green)"/>
        <ellipse cx="420" cy="425" rx="230" ry="16" fill="var(--wash-blue)"/>
        <ellipse cx="120" cy="450" rx="240" ry="20" fill="var(--wash-green)"/>
      </g>
    </svg>

    <div class="brand-mark" aria-hidden="true"></div>
    <h2 class="brand-name">
      <span class="brand-name__main">Willowbank</span>
      <span class="brand-name__sub">Dental Care</span>
    </h2>
  </section>

</body>
</html>
```